we need PDF and print ready letterheads, dupplicated 5 times with different company details of different companies. All the companies are properties developments and no need for fancy logos (any reasonable shape is ok). Then simply change the companies details (names and company number) and the colour scheme slightly. I will supply the details.

The print ready should be 300dpi, and must have cropped marks.

Should be an easy job!

```html
<!DOCTYPE html>
<html lang="en">
<head>
<meta charset="utf-8">
<title>Letterhead</title>
<link rel="stylesheet" href="https://fonts.googleapis.com/css2?family=Jost:wght@500;600&family=Open+Sans:wght@300;400&family=Montserrat:wght@400;600&display=swap">
<style>
  :root {
    --mint-light: #b0ddc9;
    --mint-mid: #84c5a9;
    --green-deep: #47997b;
    --ink: #262d31;
    --body: #3d4448;
    --accent: #1e88e5;
    --paper: #ffffff;
  }
  * { margin: 0; padding: 0; box-sizing: border-box; }
  html, body { width: 927px; height: 1200px; overflow: hidden; background: var(--paper); }
  .letterhead { position: relative; width: 927px; height: 1200px; background: var(--paper); overflow: hidden; font-family: "Open Sans", sans-serif; color: var(--body); }
  .header-bands { position: absolute; left: 0; top: 0; }
  .contact-list { position: absolute; right: 26px; top: 18px; list-style: none; text-align: right; color: var(--paper); font-family: "Open Sans", sans-serif; font-weight: 300; font-size: 19px; }
  .contact-list li { display: flex; justify-content: flex-end; align-items: center; gap: 14px; height: 30px; margin-bottom: 3px; }
  .contact-list li:last-child { margin-top: 4px; }
  .contact-list svg { width: 17px; height: 17px; }
  .brand { position: absolute; left: 548px; top: 164px; width: 260px; text-align: center; }
  .brand-square { display: block; margin: 0 auto 12px; width: 30px; height: 30px; background: var(--accent); }
  .brand-name { font-family: "Jost", sans-serif; font-weight: 500; font-size: 28px; color: var(--ink); letter-spacing: 0.2px; }
  .headline { position: absolute; left: 128px; top: 278px; font-family: "Jost", sans-serif; font-weight: 600; font-size: 45px; color: var(--ink); letter-spacing: 0.5px; }
  .body-text { position: absolute; left: 128px; font-weight: 300; color: var(--body); }
  .body-text.intro { top: 346px; font-size: 19.3px; line-height: 23.8px; }
  .body-text.second { top: 494px; font-size: 20.6px; line-height: 25.6px; }
  .body-text.third { top: 648px; font-size: 20.6px; line-height: 25.6px; }
  .subhead { position: absolute; left: 129px; top: 585px; font-family: "Jost", sans-serif; font-weight: 500; font-size: 29px; color: var(--ink); letter-spacing: 0.3px; }
  .skyline { position: absolute; left: 52px; top: 955px; width: 845px; height: 245px; background: linear-gradient(to top, var(--green-deep) 0%, var(--mint-mid) 45%, rgba(176,221,201,0.55) 100%); }
  .closing { position: absolute; left: 129px; top: 877px; font-size: 15.5px; font-weight: 400; color: var(--body); }
  .signature { position: absolute; left: 126px; top: 905px; width: 190px; height: 66px; background: linear-gradient(90deg, #e9eeec, #d9e0dd); border-radius: 4px; }
  .signer-role { position: absolute; left: 129px; top: 974px; font-size: 15.5px; font-weight: 400; color: var(--body); }
  .sender { position: absolute; right: 103px; top: 870px; text-align: right; }
  .sender-name { font-family: "Montserrat", sans-serif; font-weight: 600; font-size: 35px; color: #111; line-height: 1.1; }
  .sender-title { font-family: "Montserrat", sans-serif; font-weight: 400; font-size: 19px; letter-spacing: 1.2px; color: var(--ink); margin-top: -2px; }
  .address { position: absolute; right: 100px; top: 958px; display: flex; align-items: center; gap: 10px; font-size: 24px; color: #111; }
  .address svg { width: 26px; height: 36px; }
</style>
</head>
<body>
<main class="letterhead">
  <svg class="header-bands" width="927" height="134" viewBox="0 0 927 134" aria-hidden="true">
    <path d="M0 0 H444 C450 60 470 110 503 134 H0 Z" fill="var(--mint-light)"/>
    <path d="M464 0 H927 V134 H566 C505 130 464 80 464 0 Z" fill="var(--green-deep)"/>
  </svg>

  <ul class="contact-list">
    <li>0300-555-014
      <svg viewBox="0 0 24 24" aria-hidden="true"><path d="M6.6 10.8a15 15 0 0 0 6.6 6.6l2.2-2.2c.3-.3.7-.4 1-.2 1.1.4 2.3.6 3.6.6.6 0 1 .4 1 1V20c0 .6-.4 1-1 1A17 17 0 0 1 3 4c0-.6.4-1 1-1h3.5c.6 0 1 .4 1 1 0 1.3.2 2.5.6 3.6.1.3 0 .7-.2 1z" fill="none" stroke="#fff" stroke-width="2"/></svg>
    </li>
    <li>@example.com
      <svg viewBox="0 0 24 24" aria-hidden="true"><rect x="2" y="5" width="20" height="14" fill="#fff"/><path d="M2 5 L12 13 L22 5" fill="none" stroke="var(--green-deep)" stroke-width="1.6"/></svg>
    </li>
    <li>www.example.com
      <svg viewBox="0 0 24 24" aria-hidden="true"><circle cx="12" cy="12" r="9" fill="none" stroke="#fff" stroke-width="2"/><path d="M3 12 H21 M12 3 C7 8 7 16 12 21 M12 3 C17 8 17 16 12 21" fill="none" stroke="#fff" stroke-width="1.6"/></svg>
    </li>
  </ul>

  <div class="brand">
    <span class="brand-square"></span>
    <span class="brand-name">COMPANY NAME</span>
  </div>

  <h1 class="headline">HEADLINE</h1>
  <p class="body-text intro">Lorem ipsum dolor sit amet, consectetuer adipiscing elit, sed diam nonummy<br>nibh euismod tincidunt ut laoreet dolore magna aliquam erat volutpat. Ut wisi<br>enim ad minim veniam, quis nostrud exerci tation ullamcorper suscipit lobor-<br>tis nisl ut aliquip ex ea commodo consequat. Duis autem vel eum iriure dolor<br>in hendrerit in vulputate velit esse molestie consequat, vel illum dolore eu</p>
  <p class="body-text second">Lorem ipsum dolor sit amet, consectetuer adipiscing elit, sed diam<br>nonummy nibh euismod tincidunt ut laoreet dolore magna aliquam erat</p>

  <h2 class="subhead">PLACE YOUR TEXT HERE</h2>
  <p class="body-text third">Lorem ipsum dolor sit amet, consectetuer adipiscing elit, sed diam<br>nonummy nibh euismod tincidunt ut laoreet dolore magna aliquam erat<br>volutpat. Ut wisi enim ad minim veniam, quis nostrud exerci tation<br>ullamcorper suscipit lobortis nisl ut aliquip ex ea commodo consequat.<br>Duis autem vel eum iriure dolor in hendrerit in vulputate velit esse mo-<br>lestie consequat, vel illum dolore eu feugiat nulla facilisis at vero eros et</p>

  <div class="skyline" role="img" aria-label="Green city skyline silhouette with towers and a ferris wheel along the bottom of the page"></div>

  <p class="closing">Regard</p>
  <div class="signature" role="img" aria-label="Handwritten signature"></div>
  <p class="signer-role">Art Director</p>

  <div class="sender">
    <p class="sender-name">Daniel Harrow</p>
    <p class="sender-title">Managing Member</p>
  </div>
  <p class="address">your address here
    <svg viewBox="0 0 24 34" aria-hidden="true"><path d="M12 1C5.9 1 1 5.9 1 12c0 8 11 21 11 21s11-13 11-21C23 5.9 18.1 1 12 1z" fill="#111"/><circle cx="12" cy="12" r="4.5" fill="#fff"/></svg>
  </p>
</main>
</body>
</html>
```